Refresh existing website - qfamdv.org

Apply these upgrades to the existing website
1. Modern Design: Update the overall aesthetic to a clean, contemporary look with bold typography,
vibrant colors, and improved visual hierarchy.
2. Mobile Optimization: Enhance responsiveness for seamless navigation on mobile devices.
3. Intuitive User Interface: Simplify navigation by reducing menu complexity and improving call-to-
action buttons.
4. SEO Optimization: Improve content for better ranking on search engines.
5. Accessibility: Ensure compliance with WCAG standards for inclusivity.
6. Faster Load Times: Optimize images and scripts for better performance.
7. Social Media Integration: Add live social media feeds to showcase community engagement.
8. Prefer html
Industry/Entity Type
Consulting
Coding
Coded - Design and coding required
Number of Pages Required
5+ page
Look and feel

```html
<!DOCTYPE html>
<html lang="en">
<head>
<meta charset="utf-8">
<title>NGHPA – National Guild of Healthcare Practice Advisors</title>
<link href="https://fonts.googleapis.com/css2?family=Poppins:wght@300;400;500;600;700&display=swap" rel="stylesheet">
<style>
:root{
  --green:#62891f;
  --green-dark:#557a18;
  --slate:#44596c;
  --slate-dark:#3a4c5d;
  --ink:#3d5064;
  --text:#5f6b76;
  --light:#f4f5f6;
  --white:#ffffff;
}
*{box-sizing:border-box;margin:0;padding:0}
html,body{width:1200px;height:4325px;overflow:hidden}
body{font-family:'Poppins',sans-serif;color:var(--text);background:var(--white);position:relative}
.abs{position:absolute}
.btn{position:absolute;display:flex;align-items:center;justify-content:center;font-size:11px;font-weight:600;letter-spacing:.3px;text-transform:uppercase;border:1.5px solid var(--ink);color:var(--ink);background:transparent}
.ph{position:absolute}
/* header */
.site-header{position:absolute;left:0;top:0;width:1200px;height:87px;background:var(--white)}
.brand{position:absolute;left:89px;top:16px;display:flex;align-items:center;gap:8px;font-size:34px;font-weight:700;color:var(--slate);letter-spacing:1px}
.brand-square{width:14px;height:14px;background:var(--green)}
.nav{position:absolute;top:36px;font-size:11.5px;font-weight:500;color:var(--ink)}
.nav.active{color:var(--green);font-weight:600}
/* hero */
.hero{position:absolute;left:0;top:87px;width:1200px;height:524px;background:var(--green)}
.hero h1{position:absolute;left:89px;top:98px;width:560px;font-size:49px;line-height:53px;font-weight:600;color:var(--white)}
.hero p{position:absolute;left:89px;top:272px;width:420px;font-size:14px;line-height:22px;color:var(--white)}
.band{position:absolute;left:0;top:611px;width:1200px;height:486px;background:var(--slate)}
.tagline{position:absolute;left:163px;top:714px;font-size:29px;line-height:36px;font-weight:600;color:var(--white)}
.service-card{position:absolute;top:866px;height:144px;background:var(--slate-dark);color:var(--white)}
.service-card.featured{border:2px solid var(--green)}
.service-card h3{position:absolute;left:117px;top:36px;font-size:15.5px;line-height:22px;font-weight:600}
.service-card a{position:absolute;left:117px;top:94px;font-size:11px;font-weight:600;text-decoration:underline;color:#b7c1ca}
.service-card.featured a{color:var(--white)}
.service-card svg{position:absolute;left:36px;top:44px}
/* about */
.about h2{position:absolute;left:601px;top:1228px;font-size:28px;font-weight:600;color:var(--ink)}
.about p{position:absolute;left:601px;top:1280px;width:455px;font-size:12.8px;line-height:21.3px}
.feature{position:absolute;top:1711px;width:280px}
.feature h3{margin-top:100px;font-size:17px;font-weight:600;color:var(--ink)}
.feature p{margin-top:12px;font-size:12.8px;line-height:19.5px}
.feature svg{position:absolute;left:0;top:0}
/* finder */
.finder{position:absolute;left:0;top:2069px;width:1200px;height:537px;background:var(--light)}
.finder h2{position:absolute;left:89px;top:132px;font-size:29px;line-height:36px;font-weight:600;color:var(--ink)}
.finder p{position:absolute;left:89px;top:222px;width:350px;font-size:12.8px;line-height:21px}
/* events */
.events{position:absolute;left:0;top:2606px;width:1200px;height:495px;background:var(--green);color:var(--white);text-align:center}
.events h2{position:absolute;left:0;width:1200px;top:84px;font-size:28px;font-weight:600}
.events p{position:absolute;left:220px;width:760px;top:140px;font-size:12.3px;line-height:19px}
.event-card{position:absolute;top:213px;width:430px;height:188px;background:var(--white);text-align:left;color:var(--ink)}
.event-card .date{position:absolute;left:200px;top:30px;padding:3px 9px;background:#eef0f2;font-size:10px;color:#444}
.event-card h3{position:absolute;left:200px;top:70px;font-size:15.5px;font-weight:500}
.event-card .venue{position:absolute;left:200px;top:106px;font-size:12px;line-height:19px;color:var(--text)}
.dot{position:absolute;width:8px;height:8px;border-radius:50%;background:rgba(255,255,255,.5)}
.dot.on{width:10px;height:10px;background:var(--white)}
/* foundation */
.foundation h2{position:absolute;left:577px;top:3278px;width:480px;font-size:29px;line-height:36px;font-weight:600;color:var(--ink)}
.foundation p{position:absolute;left:577px;top:3374px;width:460px;font-size:12.8px;line-height:21px}
.sponsor{position:absolute;top:3712px;font-size:25px;font-weight:600;color:var(--slate)}
/* footer */
.site-footer{position:absolute;left:0;top:3856px;width:1200px;height:469px;background:var(--slate);color:var(--white)}
.site-footer h4{position:absolute;font-size:23px;font-weight:600}
.foot-links{position:absolute;top:146px;font-size:11.6px;line-height:25px;list-style:none;color:#e2e7ec}
.contact-line{position:absolute;left:922px;font-size:11.6px;line-height:19px;color:#e2e7ec}
.social{position:absolute;top:242px;width:38px;height:38px;background:rgba(255,255,255,.12)}
</style>
</head>
<body>

<header class="site-header">
  <div class="brand"><span class="brand-square"></span>NGHPA</div>
  <span class="nav active" style="left:347px">HOME</span>
  <span class="nav" style="left:406px">ABOUT US ˅</span>
  <span class="nav" style="left:487px">SERVICES ˅</span>
  <span class="nav" style="left:564px">FIND A CONSULTANT</span>
  <span class="nav" style="left:703px">CURRENT PODCASTS</span>
  <span class="nav" style="left:844px">MEMBER LOGIN</span>
  <svg class="abs" style="left:947px;top:37px" width="13" height="13" viewBox="0 0 13 13"><circle cx="5.5" cy="5.5" r="4.2" fill="none" stroke="#3d5064" stroke-width="1.6"/><line x1="8.6" y1="8.6" x2="12" y2="12" stroke="#3d5064" stroke-width="1.6"/></svg>
  <div class="btn" style="left:988px;top:23px;width:123px;height:42px">Contact Us</div>
</header>

<section class="hero">
  <h1>National Guild of Healthcare Practice Advisors</h1>
  <p>Annually, the NGHPA holds one advanced professional training retreat and one conference in great destination cities because education.</p>
  <div class="btn" style="left:89px;top:364px;width:183px;height:48px;border-color:#fff;color:#fff">Find a Consultant</div>
  <span class="dot" style="left:89px;top:475px;width:7px;height:7px"></span>
  <span class="dot on" style="left:104px;top:474px;width:9px;height:9px"></span>
  <span class="dot" style="left:121px;top:475px;width:7px;height:7px"></span>
</section>

<section class="band">
  <svg class="abs" style="left:87px;top:108px" width="56" height="50" viewBox="0 0 56 50"><path d="M28 46 L6 24 A12 12 0 0 1 28 8 A12 12 0 0 1 50 24 Z" fill="none" stroke="#fff" stroke-width="2.2"/><polyline points="2,26 18,26 22,18 27,32 31,22 34,26 54,26" fill="none" stroke="#8fbf3a" stroke-width="2.2"/></svg>
</section>
<div class="tagline">We are the Professionals in<br>the Business of Healthcare</div>

<div class="abs" style="left:673px;top:193px;width:461px;height:584px;border:2px solid #fff"></div>
<div class="ph" role="img" aria-label="Photo of three colleagues reviewing work on a laptop" style="left:649px;top:168px;width:462px;height:587px;background:linear-gradient(150deg,#c9c3bb,#8d8a87 55%,#5c5a5c)"></div>

<div class="service-card" style="left:87px;width:331px">
  <svg width="52" height="52" viewBox="0 0 52 52" fill="none" stroke="#fff" stroke-width="1.8"><rect x="3" y="3" width="46" height="32" rx="2"/><circle cx="14" cy="44" r="4"/><circle cx="26" cy="44" r="4"/><circle cx="38" cy="44" r="4"/><line x1="10" y1="12" x2="42" y2="12"/><line x1="10" y1="20" x2="34" y2="20"/></svg>
  <h3>Medicare Quarterly<br>Updates Webinars</h3><a>READ MORE</a>
</div>
<div class="service-card featured" style="left:438px;width:329px">
  <svg width="52" height="52" viewBox="0 0 52 52" fill="none" stroke="#8fbf3a" stroke-width="1.8"><rect x="8" y="3" width="36" height="46" rx="2"/><circle cx="26" cy="21" r="7"/><line x1="16" y1="36" x2="36" y2="36"/><line x1="16" y1="42" x2="32" y2="42"/></svg>
  <h3>NGHPA Video<br>Catalog</h3><a>READ MORE</a>
</div>
<div class="service-card" style="left:782px;width:329px">
  <svg width="60" height="52" viewBox="0 0 60 52" fill="none" stroke="#fff" stroke-width="1.8"><circle cx="30" cy="13" r="11"/><line x1="25" y1="18" x2="25" y2="12"/><line x1="30" y1="18" x2="30" y2="8"/><line x1="35" y1="18" x2="35" y2="14"/><circle cx="12" cy="34" r="5"/><circle cx="30" cy="34" r="5"/><circle cx="48" cy="34" r="5"/><path d="M3 50 v-6 a9 6 0 0 1 18 0 v6 M21 50 v-6 a9 6 0 0 1 18 0 v6 M39 50 v-6 a9 6 0 0 1 18 0 v6"/></svg>
  <h3>Practice Benchmark<br>Reports</h3><a>READ MORE</a>
</div>

<section class="about">
  <div class="ph" role="img" aria-label="Photo of a doctor and patient looking at a clipboard" style="left:180px;top:1175px;width:359px;height:456px;background:linear-gradient(160deg,#dcdcdc,#b9b2a8 60%,#6f6a55)"></div>
  <div class="abs" style="left:141px;top:1488px;width:74px;height:74px;background:var(--green)"><svg width="74" height="74" viewBox="0 0 74 74"><polygon points="32,30 44,37 32,44" fill="#fff"/></svg></div>
  <h2>About NGHPA</h2>
  <p>For nearly 30 years, the National Guild of Healthcare Practice Advisors (NGHPA) and its originating organizations have provided an active forum for networking and knowledge sharing. NGHPA provides members with an in-depth understanding of the constantly changing healthcare business environment – both medical and dental – that is unavailable anywhere else. At our core is the belief that knowledge is gained via continuous professional development, which grows exponentially when we share it with our fellow members through the exchange of insights and best practices. In turn, this helps deliver unparalleled benefits to our members and their clients.</p>
  <div class="btn" style="left:601px;top:1537px;width:132px;height:42px">Read More</div>

  <div class="feature" style="left:136px">
    <svg width="76" height="70" viewBox="0 0 76 70" fill="none" stroke="#62891f" stroke-width="2"><circle cx="38" cy="16" r="13"/><circle cx="16" cy="50" r="13"/><circle cx="60" cy="50" r="13"/><circle cx="38" cy="13" r="4"/><circle cx="16" cy="47" r="4"/><circle cx="60" cy="47" r="4"/></svg>
    <h3>Member Toolbox</h3><p>NGHPA members also benefit from an exclusive set of resources known as our Member Toolbox. The Toolbox is...</p>
  </div>
  <div class="feature" style="left:461px">
    <svg width="72" height="72" viewBox="0 0 72 72" fill="none" stroke="#62891f" stroke-width="2"><rect x="4" y="4" width="46" height="60" rx="2"/><line x1="12" y1="16" x2="42" y2="16"/><line x1="12" y1="26" x2="36" y2="26"/><line x1="12" y1="36" x2="30" y2="36"/><circle cx="52" cy="42" r="12"/><polyline points="46,54 44,70 52,64 60,70 58,54"/></svg>
    <h3>Certification Program</h3><p>The NGHPA keeps members on the leading edge of healthcare business counseling through our globally...</p>
  </div>
  <div class="feature" style="left:787px">
    <svg width="60" height="72" viewBox="0 0 60 72" fill="none" stroke="#62891f" stroke-width="2"><rect x="4" y="2" width="52" height="68" rx="2"/><line x1="14" y1="36" x2="14" y2="28"/><line x1="22" y1="36" x2="22" y2="20"/><line x1="30" y1="36" x2="30" y2="24"/><line x1="38" y1="36" x2="38" y2="14"/><line x1="10" y1="40" x2="50" y2="40"/><circle cx="18" cy="54" r="7"/><line x1="30" y1="50" x2="48" y2="50"/><line x1="30" y1="58" x2="44" y2="58"/></svg>
    <h3>Practice Benchmarks Report</h3><p>One of the key tools that we use to facilitate that dialogue is the gathering of medical and dental income and...</p>
  </div>
  <div class="btn" style="left:137px;top:1930px;width:132px;height:43px">Read More</div>
  <div class="btn" style="left:462px;top:1930px;width:130px;height:43px">Read More</div>
  <div class="btn" style="left:788px;top:1930px;width:130px;height:43px">Read More</div>
</section>

<section class="finder">
  <h2>Find an NGHPA Healthcare<br>Business Consultant</h2>
  <p>For state search criteria, select "contains"in the drop down menu Click Enter after all search criteria have been entered:</p>
  <div class="btn" style="left:89px;top:309px;width:216px;height:49px">Get in Touch With Us</div>
  <div class="ph" role="img" aria-label="Photo of three smiling consultants standing with arms crossed" style="left:487px;top:67px;width:649px;height:470px;background:radial-gradient(ellipse at 50% 60%,#9aa3ad,#c9cdd2 60%,#f4f5f6 80%)"></div>
</section>

<section class="events">
  <h2>Upcoming Education Events</h2>
  <p>Annually, the NGHPA holds one advanced professional training retreat and one conference in great destination cities because education is one of the key tenets from which we learn and share knowledge.</p>
  <div class="event-card" style="left:151px">
    <div class="ph" role="img" aria-label="Photo of a beach resort" style="left:0;top:0;width:177px;height:188px;background:linear-gradient(180deg,#9ec3dd,#d6b9a7 55%,#e9e4da)"></div>
    <span class="date">January 9-10, 2025</span>
    <h3>2025 Consultants Retreat</h3>
    <div class="venue">The Coral Tide Resort &amp;<br>Marina Seabright Beach, FL</div>
    <svg class="abs" style="left:200px;top:150px" width="18" height="12" viewBox="0 0 18 12" fill="none" stroke="#3d5064" stroke-width="1.4"><line x1="1" y1="6" x2="16" y2="6"/><polyline points="11,1 16,6 11,11"/></svg>
  </div>
  <div class="event-card" style="left:621px">
    <div class="ph" role="img" aria-label="Photo of a city skyline" style="left:0;top:0;width:177px;height:188px;background:linear-gradient(180deg,#c9d6e2,#8c99a6 60%,#4f5a64)"></div>
    <span class="date">June 4-6, 2025</span>
    <h3>2025 Annual Conference</h3>
    <div class="venue">The Halloway<br>Riverton, GA</div>
    <svg class="abs" style="left:200px;top:150px" width="18" height="12" viewBox="0 0 18 12" fill="none" stroke="#3d5064" stroke-width="1.4"><line x1="1" y1="6" x2="16" y2="6"/><polyline points="11,1 16,6 11,11"/></svg>
  </div>
  <span class="dot" style="left:578px;top:452px;width:7px;height:7px"></span>
  <span class="dot on" style="left:594px;top:451px;width:9px;height:9px"></span>
  <span class="dot" style="left:611px;top:452px;width:7px;height:7px"></span>
</section>

<section class="foundation">
  <div class="abs" style="left:165px;top:3242px;width:362px;height:362px;border-radius:50%;background:#eceef0"></div>
  <div class="abs" style="left:245px;top:3195px;width:201px;height:409px;border-radius:26px;background:#2b2f33"></div>
  <div class="ph" role="img" aria-label="App screen showing doctors at work" style="left:255px;top:3212px;width:181px;height:375px;border-radius:16px;background:linear-gradient(180deg,#f7f8f8 20%,#cfd6d9 40%,#9aa8ae)"></div>
  <div class="abs" style="left:265px;top:3262px;width:161px;text-align:center;font-size:24px;font-weight:700;color:var(--slate)">NGHPA</div>
  <h2>The Fund for Learning in Practice Management</h2>
  <p>The Fund for Learning in Practice Management is a non-profit organization dedicated to improving healthcare delivery through the education of practice management consultants.</p>
  <div class="btn" style="left:577px;top:3472px;width:128px;height:42px">Read More</div>
  <div class="btn" style="left:716px;top:3472px;width:130px;height:42px;border-color:var(--green);color:var(--green)">Donate</div>
</section>

<div class="abs" style="left:89px;top:3708px;font-size:17px;font-weight:600;line-height:18px;color:var(--slate)">Thank You!<br><span style="font-size:10px">to our Sponsors</span></div>
<span class="sponsor" style="left:272px">Brightpath</span>
<span class="sponsor" style="left:458px">Tri Ledger</span>
<span class="sponsor" style="left:651px">Curanta</span>
<span class="sponsor" style="left:843px">Clearward</span>
<span class="sponsor" style="left:1016px">Helmo</span>

<footer class="site-footer">
  <div class="abs" style="left:121px;top:150px;width:273px;text-align:center;font-size:44px;font-weight:700;color:#fff;letter-spacing:2px">NGHPA</div>
  <div class="social" style="left:163px"></div>
  <div class="social" style="left:214px;background:var(--green)"></div>
  <div class="social" style="left:265px"></div>
  <div class="social" style="left:316px"></div>
  <div class="abs" style="left:448px;top:80px;width:1px;height:200px;background:rgba(255,255,255,.2)"></div>
  <div class="abs" style="left:844px;top:80px;width:1px;height:200px;background:rgba(255,255,255,.2)"></div>
  <h4 style="left:503px;top:86px">Quick Links</h4>
  <ul class="foot-links" style="left:503px"><li>Home</li><li>Get Certified (CHPA)</li><li>Find A Consultant</li><li>Current News</li><li>Current Podcasts</li><li>Member Login</li><li>About the Society</li></ul>
  <ul class="foot-links" style="left:673px"><li>About Membership</li><li>Products/Services</li><li>Upcoming Education</li><li>Practice Reports</li><li>Foundation (FLPM)</li><li>NGHPA Sponsors</li><li>Contact Us</li></ul>
  <h4 style="left:901px;top:86px">Contact Us</h4>
  <svg class="abs" style="left:901px;top:149px" width="11" height="14" viewBox="0 0 11 14"><path d="M5.5 13 C2 8 1 6.5 1 5 a4.5 4.5 0 0 1 9 0 c0 1.5-1 3-4.5 8z" fill="#fff"/><circle cx="5.5" cy="5" r="1.6" fill="#44596c"/></svg>
  <div class="contact-line" style="top:146px">NGHPA<br>480 Harbor Point Way<br>#212<br>Alder Creek, VA 20999</div>
  <svg class="abs" style="left:900px;top:232px" width="12" height="12" viewBox="0 0 12 12"><path d="M2 1 l2.5 0 1 3 -1.5 1 a7 7 0 0 0 3 3 l1 -1.5 3 1 0 2.5 a1 1 0 0 1-1 1 A10 10 0 0 1 1 2 a1 1 0 0 1 1-1z" fill="#fff"/></svg>
  <div class="contact-line" style="top:229px">Tel: 555-201-3344</div>
  <svg class="abs" style="left:900px;top:259px" width="12" height="12" viewBox="0 0 12 12"><rect x="3" y="1" width="6" height="3" fill="#fff"/><rect x="1" y="4" width="10" height="5" fill="#fff"/><rect x="3" y="8" width="6" height="3" fill="#fff"/></svg>
  <div class="contact-line" style="top:256px">Fax: 555-201-3390</div>
  <svg class="abs" style="left:900px;top:287px" width="12" height="10" viewBox="0 0 12 10"><rect x="0" y="0" width="12" height="10" fill="#fff"/><polyline points="0,0 6,5 12,0" fill="none" stroke="#44596c" stroke-width="1.2"/></svg>
  <div class="contact-line" style="top:283px">info@qfamdv.org</div>
  <div class="abs" style="left:89px;top:393px;width:1022px;height:1px;background:rgba(255,255,255,.2)"></div>
  <div class="abs" style="left:121px;top:418px;font-size:11px;color:#e2e7ec">©2024 National Guild of Healthcare Practice Advisors</div>
  <div class="abs" style="left:816px;top:418px;font-size:11px;color:#e2e7ec;word-spacing:2px">Privacy Policy&nbsp;&nbsp;&nbsp;&nbsp;Site Disclaimer&nbsp;&nbsp;&nbsp;&nbsp;Sitemap</div>
  <div class="abs" style="left:1136px;top:357px;width:39px;height:38px;background:var(--green)"><svg width="39" height="38" viewBox="0 0 39 38" fill="none" stroke="#fff" stroke-width="1.5"><line x1="19.5" y1="26" x2="19.5" y2="12"/><polyline points="14,17 19.5,12 25,17"/></svg></div>
</footer>

</body>
</html>
```